Album Artwork Design for Industrial/Experimental music project

Artist: Glumwirecask. Album name: Velvet Ladder Fever. At the core of the design can be an outburst, emotions, something intense and vivid. The main idea is to portray the view of some blown up toys from the camera dropped to the ground (with a couple of blood drops on the lens). Another theme for inspiration can be the nuclear mushroom inside a cracked snow globe with bloody snow
maybe also try adding some light that comes out of the cracks in the snow globe. Also this description shouldn’t stop you from trying your own ideas.

Industry/Entity Type

Industrial

Requirements
Must have
• Artist and Album Titles

```html
<!DOCTYPE html>
<html lang="en">
<head>
<meta charset="utf-8">
<title>Glumwirecask — Velvet Ladder Fever</title>
<link rel="stylesheet" href="https://fonts.googleapis.com/css2?family=Orbitron:wght@900&family=Archivo+Black&display=swap">
<style>
  :root {
    --page-bg: #e6e6e6;
    --cover-border: #ffffff;
    --art-hot: #f4d6cc;
    --art-red: #e0141a;
    --art-deep: #7a0a0c;
    --art-black: #0a0203;
    --artist-white: #ffffff;
    --title-gold: #d9a01c;
  }
  * { margin: 0; padding: 0; box-sizing: border-box; }
  html, body {
    width: 1200px;
    height: 848px;
    overflow: hidden;
    background: var(--page-bg);
  }
  .album-cover {
    position: absolute;
    left: 276px;
    top: 100px;
    width: 648px;
    height: 648px;
    border: 3px solid var(--cover-border);
    box-shadow: 2px 3px 6px rgba(0, 0, 0, 0.45);
    overflow: hidden;
    background: var(--art-black);
  }
  .cover-art {
    position: absolute;
    inset: 0;
    background:
      radial-gradient(ellipse 28% 22% at 42% 30%, var(--art-hot) 0%, rgba(244,214,204,0) 100%),
      radial-gradient(ellipse 60% 45% at 45% 30%, var(--art-red) 0%, rgba(224,20,26,0.85) 45%, rgba(122,10,12,0.6) 75%, rgba(10,2,3,0) 100%),
      radial-gradient(ellipse 80% 60% at 50% 45%, var(--art-deep) 0%, var(--art-black) 100%);
  }
  .cover-text {
    position: absolute;
    inset: 0;
  }
  .artist-name {
    font-family: "Orbitron", sans-serif;
    font-weight: 900;
    fill: var(--artist-white);
  }
  .album-title {
    font-family: "Archivo Black", sans-serif;
    fill: var(--title-gold);
  }
</style>
</head>
<body>
  <div class="album-cover">
    <div class="cover-art" role="img" aria-label="Grungy red and white explosion burst bursting from a dark textured background"></div>
    <svg class="cover-text" width="642" height="642" viewBox="0 0 642 642" xmlns="http://www.w3.org/2000/svg">
      <text class="artist-name" x="34" y="338" font-size="66" textLength="582" lengthAdjust="spacingAndGlyphs">GLUMWIRECASK</text>
      <g class="album-title" font-size="37">
        <text x="36" y="432" textLength="178" lengthAdjust="spacingAndGlyphs">VELVET</text>
        <text x="36" y="474" textLength="178" lengthAdjust="spacingAndGlyphs">LADDER</text>
        <text x="36" y="516" textLength="168" lengthAdjust="spacingAndGlyphs">FEVER</text>
      </g>
    </svg>
  </div>
</body>
</html>
```